wardrobe/costume stylist needs good business card for own business

Hi:)

I'm wanting a business card for my company. I am a freelance stylist.

I do wardrobe/costume stylist to TV commercials; Films; Fashion and Lifestyle shoots.

I'd like a design based around my name Rosalind Pember written nicely, maybe a colour? Up to you?!

I've attached a couple of images of business cards I like
.... be creative and have fun!

Thank you :)
Updates

Reason: I was trying to get my new business card ready for before I headed overseas Friday morning but I don't think that was realistic so I'd like to extend the deadline to give time to the project. Thank you

Hi designers:) Thank you for all your designs, I've extended the deadline until Sunday, so there's a bit more time. I've attached 3 pictures of business cards which I quite like, please take a look to see if it can be of help in your process. I like the pale plain or patterned background with dark font and the dark plain or patterned background with the pale font the motifs the feminine fonts the plain fonts I like the idea of playing with a circle or some shape on one side of the card with my name or initials as in the picture I have on my post could you play around with this idea a bit please? Thank you all for the work you've done :) Rosa

Hi I am working overseas til Saturday night sorry for no feedback until I teturn Thanks :) Rosa

Hi designers, Thank you all so much for submitting your designs, I really appreciate your input into my project :) I'm sorry I didn't get to respond to some comments, and give feedback. I didn't back from being away until later than I expected, and the deadline had passed then, so apologies. Thanks to you all again for all your really good designs :) Rosa

Target Market(s)

I am a freelance stylist my target audience is producers, production companies, photographers, directors...

Industry/Entity Type

Business

Requirements
Must have
• Rosalind Pember
Stylist or Wardrobe Stylist

email rosapember@quillnet.co.nz
Mobile 0218846193

(Don't have to use the words 'email' and 'mobile')
Nice to have
• Would like it to be double sided
Like B & W
Like pale colour background with dark font or white font
Like dark colour background with pale font
Should not have
• I would prefer it not to incorporate pictures

```html
<!DOCTYPE html>
<html lang="en">
<head>
<meta charset="utf-8">
<title>Rosalind Pember — Wardrobe Stylist Business Card</title>
<link rel="stylesheet" href="https://fonts.googleapis.com/css2?family=Marcellus&display=swap">
<style>
  :root {
    --page: #ffffff;
    --mint: #b4e0cb;
    --mint-light: #d3efe2;
    --ink: #141414;
    --night: #0b0b0b;
    --night-glow: #2b2b2b;
    --mint-text: #bfe6d4;
    --silver: #c9cfcc;
    --card-w: 520px;
    --card-h: 300px;
    --radius: 26px;
  }
  * { box-sizing: border-box; margin: 0; padding: 0; }
  html, body {
    width: 1200px;
    height: 900px;
    overflow: hidden;
    background: var(--page);
  }
  .canvas {
    position: relative;
    width: 1200px;
    height: 900px;
    display: flex;
    justify-content: center;
    align-items: center;
    gap: 40px;
    font-family: "Marcellus", "Times New Roman", serif;
  }
  .card {
    position: relative;
    width: var(--card-w);
    height: var(--card-h);
    border-radius: var(--radius);
    display: flex;
    flex-direction: column;
    align-items: center;
    justify-content: center;
    text-align: center;
    box-shadow: 0 18px 30px rgba(0, 0, 0, 0.12);
  }
  .card--front {
    background: radial-gradient(ellipse at 50% 45%, var(--mint-light) 0%, var(--mint) 60%);
    color: var(--ink);
  }
  .card--back {
    background: radial-gradient(ellipse at 50% 45%, var(--night-glow) 0%, var(--night) 70%);
    color: var(--mint-text);
  }
  .ornament {
    border-radius: 50%;
  }
  .card--front .ornament {
    width: 150px;
    height: 52px;
    background: radial-gradient(ellipse at center, var(--ink) 0%, rgba(20, 20, 20, 0.75) 45%, rgba(180, 224, 203, 0) 72%);
  }
  .card--back .ornament {
    width: 80px;
    height: 30px;
    background: radial-gradient(ellipse at center, var(--mint-text) 0%, rgba(191, 230, 212, 0.7) 45%, rgba(11, 11, 11, 0) 72%);
  }
  .name {
    font-weight: 400;
    line-height: 1;
  }
  .card--front .name {
    font-size: 46px;
    margin-top: 8px;
  }
  .card--back .name {
    font-size: 24px;
    margin-top: 4px;
  }
  .role {
    font-weight: 400;
    line-height: 1;
  }
  .card--front .role {
    font-size: 13px;
    letter-spacing: 10px;
    margin: 4px 0 8px 10px;
  }
  .card--back .role {
    font-size: 8px;
    letter-spacing: 5px;
    margin: 3px 0 4px 5px;
  }
  .contact {
    margin-top: 30px;
    color: var(--silver);
    font-style: normal;
    line-height: 1.45;
  }
  .contact__phone {
    display: block;
    font-size: 16px;
    letter-spacing: 4px;
  }
  .contact__email {
    display: block;
    font-size: 15px;
    letter-spacing: 2px;
  }
</style>
</head>
<body>
  <main class="canvas">
    <section class="card card--front" aria-label="Card front">
      <div class="ornament" role="img" aria-label="Dark damask flourish ornament above the name"></div>
      <h1 class="name">Rosalind Pember</h1>
      <p class="role">Wardrobe Stylist</p>
      <div class="ornament" role="img" aria-label="Dark damask flourish ornament below the name"></div>
    </section>

    <section class="card card--back" aria-label="Card back">
      <div class="ornament" role="img" aria-label="Mint damask flourish ornament above the name"></div>
      <h2 class="name">Rosalind Pember</h2>
      <p class="role">Wardrobe Stylist</p>
      <div class="ornament" role="img" aria-label="Mint damask flourish ornament below the name"></div>
      <address class="contact">
        <span class="contact__phone">0218846193</span>
        <span class="contact__email">rosapember@quillnet.co.nz</span>
      </address>
    </section>
  </main>
</body>
</html>
```